Business Card Design Project

I need a business card design for an Organic drive thru coffee kiosk. We will serve organic coffee, teas & smoothies and will serve healthy breakfast food/snacks for people on the go.
I want the card to have 2-3 colors max (earthy colors like browns, greens and so on).
I have attached the logo I want used and would love to play off the theme of "balance."
Include:
Tidy-Kettle Coffee
address: 4820 Gorvin Ct. Raleigh, NC 27583
phone: 919-731-4062
website: www.tidy-kettle.com (website is not up yet but still include it on card)
email: Rosalind@tidy-kettle.com
I want one of the following sayings somewhere on the card (the front or back is fine):
"Break the fast with Tidy-Kettle"
"Break the fast with Tidy-Kettle"
Maybe on the back list what we offer:
-Organic coffee, espresso & tea
-Blendora smoothies & protein shakes
-Zesty Pour (100% fresh local fruit and veggies)
-Tender Nibs

```html
<!DOCTYPE html>
<html lang="en">
<head>
<meta charset="utf-8">
<title>Tidy-Kettle Coffee – Business Card</title>
<link rel="stylesheet" href="https://fonts.googleapis.com/css2?family=Ubuntu:ital,wght@0,400;0,500;1,400&display=swap">
<style>
  :root {
    --bg: #ece7e1;
    --espresso: #4b2a1f;
    --espresso-deep: #3f2219;
    --rust: #8b3d26;
    --paper: #ffffff;
    --ink: #3a2219;
    --cream: #f6eee6;
  }
  * { box-sizing: border-box; margin: 0; padding: 0; }
  html, body {
    width: 1200px; height: 900px; overflow: hidden;
    background: var(--bg);
    font-family: "Ubuntu", sans-serif;
  }
  .canvas { position: relative; width: 1200px; height: 900px; }
  .card {
    position: absolute; left: 260px; width: 680px; height: 390px;
    border-radius: 26px; overflow: hidden;
    box-shadow: 0 10px 26px rgba(60, 35, 20, .18);
  }
  /* back side */
  .card--back { top: 45px; background: var(--espresso); }
  .back-disc {
    position: absolute; left: -90px; top: 150px;
    width: 330px; height: 330px; border-radius: 50%;
    background: var(--rust);
  }
  .offer-list {
    position: absolute; left: 300px; top: 110px; width: 360px;
    list-style: none; color: var(--cream);
    font-size: 19px; line-height: 1.45;
  }
  .offer-list li { padding-left: 18px; position: relative; }
  .offer-list li::before { content: "•"; position: absolute; left: 0; }
  /* front side */
  .card--front { top: 465px; background: var(--paper); }
  .brand { position: absolute; left: 52px; top: 70px; width: 280px; text-align: center; }
  .brand-dot {
    width: 58px; height: 58px; border-radius: 50%;
    background: var(--rust); margin: 0 auto 10px;
  }
  .brand-name { font-size: 48px; font-weight: 500; color: var(--espresso); letter-spacing: -.5px; line-height: 1; }
  .brand-tagline {
    margin-top: 10px; font-size: 14px; letter-spacing: 3px;
    color: var(--rust); text-transform: uppercase;
  }
  .slogan-band {
    position: absolute; left: 0; top: 278px; width: 330px; height: 36px;
    background: var(--espresso-deep); border-radius: 0 10px 10px 0;
    color: var(--paper); font-style: italic; font-size: 18px;
    line-height: 36px; padding-left: 36px; white-space: nowrap;
  }
  .contact { position: absolute; left: 380px; top: 92px; width: 280px; color: var(--ink); }
  .contact-name { font-size: 24px; font-weight: 500; letter-spacing: .5px; text-transform: uppercase; white-space: nowrap; }
  .contact-role { font-size: 15px; margin-top: 2px; }
  .contact-lines { margin-top: 26px; font-size: 17px; line-height: 1.35; }
  .contact-lines dt { float: left; width: 24px; font-style: italic; font-weight: 500; }
  .contact-lines dd { margin-left: 24px; }
  .contact-address { margin-top: 14px; font-size: 17px; white-space: nowrap; }
  .contact-web { margin-top: 16px; font-size: 17px; }
</style>
</head>
<body>
<main class="canvas">
  <section class="card card--back" aria-label="Card back">
    <div class="back-disc"></div>
    <ul class="offer-list">
      <li>Organic coffee, espresso &amp; tea</li>
      <li>Blendora smoothies &amp; protein shakes</li>
      <li>Zesty Pour (100% fresh local<br>fruit and veggies)</li>
      <li>Tender Nibs</li>
    </ul>
  </section>

  <section class="card card--front" aria-label="Card front">
    <div class="brand">
      <div class="brand-dot"></div>
      <div class="brand-name">Tidy-Kettle</div>
      <div class="brand-tagline">Organic Coffee + Cafe</div>
    </div>
    <div class="slogan-band">Break the fast with Tidy-Kettle</div>

    <div class="contact">
      <div class="contact-name">Rosalind Hartwell</div>
      <div class="contact-role">Operation Manager</div>
      <dl class="contact-lines">
        <dt>T</dt><dd>919-731-4062</dd>
        <dt>E</dt><dd>rosalind@tidy-kettle.com</dd>
      </dl>
      <div class="contact-address">4820 Gorvin Ct. Raleigh, NC 27583</div>
      <div class="contact-web">www.tidy-kettle.com</div>
    </div>
  </section>
</main>
</body>
</html>
```